Cleaners Needs Bounce-Back Coupon For Laundry Service

We need a "bounce-back" coupon to attach to peoples dry cleaning orders that offers one free wash-n-fold laundry service. Right now we always attach their receipt to the bag that contains their dry cleaning when we return it. We'd like to also attach a coupon that will entice them to come try our laundry service.

Background on the service: We sort, wash, dry, and fold the laundry for customers and then neatly put it in a nice bag that makes returning very convenient. Their laundry comes out fresh, clean, smelling great, and without the hassle of doing it themselves. We have a great return rate. Most customers that try out the service become long term customers. The goal is to get our dry cleaning customers to come try it out.

Requirements:
* 5" x 8" and one-sided.
* To be printed on a standard color of card stock.
* Must incorporate our logo.
* Needs a place for us to fill in an expiration date. We'll fill in a date about two weeks out from the time they pick up their dry cleaning.
* Limit one coupon per customer.
* Limit 50 pounds of laundry per coupon.

Industry/Entity Type

Dry Cleaning

```html
<!DOCTYPE html>
<html lang="en">
<head>
<meta charset="UTF-8">
<title>Suds Street Laundry – Wash-n-Fold Coupon</title>
<link rel="stylesheet" href="https://fonts.googleapis.com/css2?family=Encode+Sans+Semi+Condensed:wght@700&family=Open+Sans:wght@400;600;700&display=swap">
<style>
  :root {
    --page: #eef0f2;
    --navy: #1f3f9e;
    --bubble: #2d4cad;
    --bubble-dark: #243f95;
    --stitch: #f39a2a;
    --red: #e8202a;
    --teal: #2f7d8c;
    --mist: #eef1fb;
    --white: #ffffff;
    --ink: #1a1a1a;
    --icon: #a7b4ea;
  }
  * { margin: 0; padding: 0; box-sizing: border-box; }
  html, body { width: 952px; height: 1200px; overflow: hidden; }
  body { background: var(--page); font-family: "Open Sans", sans-serif; position: relative; }

  .coupon {
    position: absolute; left: 126px; top: 40px; width: 700px; height: 1120px;
    overflow: hidden;
    background: linear-gradient(180deg, var(--teal) 272px, #7fb0c0 340px, #d4def0 440px, var(--mist) 600px, var(--white) 1120px);
  }
  .shirts-photo {
    position: absolute; left: 0; top: 0; width: 700px; height: 272px;
    background: linear-gradient(90deg, #dfe6ef 0%, #b9c9dc 22%, #2c3f66 45%, #6f8fc0 62%, #cfdced 80%, #eef2f7 100%);
  }
  .brand {
    position: absolute; left: 36px; top: 318px; display: flex; align-items: center; gap: 20px;
    white-space: nowrap;
  }
  .brand-mark { width: 58px; height: 58px; background: var(--navy); flex: none; }
  .brand-name {
    font-family: "Open Sans", sans-serif; font-weight: 700; font-size: 52px; line-height: 1.2;
    color: var(--navy); letter-spacing: -0.5px;
  }
  .headline {
    position: absolute; left: 0; width: 700px; top: 496px; text-align: center; white-space: nowrap;
    font-family: "Encode Sans Semi Condensed", sans-serif; font-weight: 700; font-size: 33px; line-height: 44px;
    color: var(--red); letter-spacing: -0.3px;
  }
  .offer-bubble { position: absolute; left: 0; top: 0; }
  .offer-amount {
    position: absolute; left: 138px; width: 160px; top: 606px; text-align: center; color: var(--red); font-weight: 700;
  }
  .offer-amount .number { display: block; font-size: 130px; line-height: 1; letter-spacing: -3px; }
  .offer-amount .unit { display: block; font-size: 33px; line-height: 1; margin-top: 2px; }
  .offer-terms {
    position: absolute; left: 335px; top: 648px; color: var(--white); font-weight: 700; font-size: 41px; line-height: 1.28;
    white-space: nowrap;
  }
  .basket-photo {
    position: absolute; left: 0; top: 890px; width: 340px; height: 230px;
    background: radial-gradient(ellipse at 40% 20%, #c9c3b8 0%, #8a7f72 35%, #5b4637 65%, #3e2d22 100%);
    border-top-right-radius: 60px;
  }
  .limit-note {
    position: absolute; left: 358px; width: 316px; top: 958px; text-align: center; font-size: 23px; line-height: 32px;
    color: var(--ink); white-space: nowrap;
  }
  .expiry-field {
    position: absolute; left: 358px; top: 996px; width: 314px; height: 62px; background: var(--white);
    border: 1px solid #cfd3dc; box-shadow: 4px 5px 6px rgba(0,0,0,0.3);
  }
  .expiry-label {
    position: absolute; left: 358px; width: 316px; top: 1068px; text-align: center; font-size: 21px; line-height: 28px;
    font-weight: 600; color: var(--ink);
  }
</style>
</head>
<body>
  <main class="coupon">
    <div class="shirts-photo" role="img" aria-label="Photo of pressed dress shirts hanging on wooden hangers"></div>

    <div class="brand">
      <span class="brand-mark"></span>
      <span class="brand-name">Suds Street Laundry</span>
    </div>

    <p class="headline">FREE WASH-N-FOLD LAUNDRY SERVICE</p>

    <svg class="offer-bubble" width="700" height="1120" viewBox="0 0 700 1120" aria-hidden="true">
      <path d="M125 562 H581 Q601 562 601 582 V808 Q601 828 581 828 H286 L179 888 L175 828 H125 Q105 828 105 808 V582 Q105 562 125 562 Z"
            fill="var(--bubble)" stroke="var(--bubble-dark)" stroke-width="3"/>
      <path d="M128 576 H578 Q587 576 587 585 V805 Q587 814 578 814 H282 L190 866 L189 814 H128 Q119 814 119 805 V585 Q119 576 128 576 Z"
            fill="none" stroke="var(--stitch)" stroke-width="2" stroke-dasharray="7 5"/>
      <g class="care-icons" fill="none" stroke="var(--icon)" stroke-width="2.5">
        <path d="M236 624 L256 596 L276 624 Z"/><path d="M240 596 L272 626 M272 596 L240 626"/>
        <path d="M292 598 L298 624 H324 L330 598"/><path d="M292 604 Q301 600 311 604 Q320 608 330 604"/>
        <rect x="346" y="597" width="28" height="28"/><circle cx="360" cy="611" r="9"/>
        <path d="M390 624 H420 V610 Q420 600 408 600 H398 Q392 604 390 624 Z"/>
        <path d="M436 624 L446 598 H466"/><path d="M436 624 H468 V610"/><path d="M438 598 L468 626 M468 598 L438 626"/>
      </g>
    </svg>

    <div class="offer-amount">
      <span class="number">50</span>
      <span class="unit">POUNDS</span>
    </div>
    <p class="offer-terms">of laundry<br>per coupon</p>

    <div class="basket-photo" role="img" aria-label="Photo of a wicker laundry basket holding rolled towels"></div>

    <p class="limit-note">(One coupon per customer)</p>
    <div class="expiry-field"></div>
    <p class="expiry-label">expiration date</p>
  </main>
</body>
</html>
```